BrimstoneHoldingsLLC

Real Estate Investment. Buy/Sell house/investment . Trustworthy,Reliable, and friendly

Industry/Entity Type

Real Estate

Contact Information for Business Card

BrimstoneHoldings@mailtrove.com
555-413-2960
Tamsin-Leigh Okafor

```html
<!DOCTYPE html>
<html lang="en">
<head>
<meta charset="utf-8">
<title>Brimstone Holdings LLC – Business Card</title>
<link href="https://fonts.googleapis.com/css2?family=Tinos:wght@400;700&display=swap" rel="stylesheet">
<style>
  :root {
    --navy: #2e2a7a;
    --red: #d9322a;
    --paper: #ffffff;
    --backdrop: #e9e6e1;
    --rule: #4a4690;
  }
  * { margin: 0; padding: 0; box-sizing: border-box; }
  html, body { width: 1200px; height: 858px; overflow: hidden; }
  body {
    background: var(--backdrop);
    font-family: "Tinos", "Times New Roman", serif;
    position: relative;
  }
  .card {
    position: absolute;
    background: var(--paper);
    box-shadow: 0 6px 18px rgba(0,0,0,0.18);
    overflow: hidden;
  }
  /* Front */
  .card-front {
    left: 70px; top: 254px; width: 560px; height: 350px;
    display: flex; flex-direction: column; align-items: center; justify-content: center;
  }
  .brand {
    display: flex; align-items: center; gap: 14px;
    color: var(--navy);
    text-transform: uppercase;
    letter-spacing: 2px;
    font-weight: 400;
  }
  .brand-mark {
    width: 22px; height: 22px; background: var(--red); flex: none;
  }
  .card-front .brand { font-size: 36px; }
  .tagline-row {
    display: flex; align-items: center; gap: 14px;
    color: var(--navy);
    font-weight: 700;
  }
  .tagline-row .rule { height: 1px; background: var(--rule); }
  .card-front .tagline-row { margin-top: 10px; font-size: 20px; }
  .card-front .tagline-row .rule { width: 70px; }
  .services {
    margin-top: 26px;
    color: var(--red);
    font-size: 24px;
  }
  /* Back */
  .card-back {
    left: 720px; top: 149px; width: 360px; height: 560px;
  }
  .back-header {
    position: absolute; top: 70px; left: 0; right: 0;
    display: flex; flex-direction: column; align-items: center;
  }
  .card-back .brand { font-size: 22px; gap: 10px; letter-spacing: 1.5px; }
  .card-back .brand-mark { width: 14px; height: 14px; }
  .card-back .tagline-row { margin-top: 6px; font-size: 12px; gap: 10px; }
  .card-back .tagline-row .rule { width: 60px; }
  .contact-name {
    position: absolute; top: 232px; left: 0; right: 0; text-align: center;
    color: var(--navy); font-size: 22px;
  }
  .contact-details {
    position: absolute; top: 320px; left: 0; right: 0; text-align: center;
    color: var(--navy); font-size: 17px; line-height: 1.35;
  }
  .back-band {
    position: absolute; left: 0; right: 0; bottom: 0; height: 78px;
    background: var(--navy);
  }
  .back-band::before {
    content: ""; position: absolute; left: 0; right: 0; top: 6px; height: 2px;
    background: var(--paper);
  }
</style>
</head>
<body>
  <section class="card card-front">
    <div class="brand"><span class="brand-mark"></span>Brimstone Holdings LLC</div>
    <div class="tagline-row"><span class="rule"></span>Real Estate Investment<span class="rule"></span></div>
    <div class="services">Buy/Sell house/investment</div>
  </section>

  <section class="card card-back">
    <div class="back-header">
      <div class="brand"><span class="brand-mark"></span>Brimstone Holdings LLC</div>
      <div class="tagline-row"><span class="rule"></span>Real Estate Investment<span class="rule"></span></div>
    </div>
    <div class="contact-name">Tamsin-Leigh Okafor</div>
    <div class="contact-details">
      <div class="phone">555-413-2960</div>
      <div class="email">BrimstoneHoldings@mailtrove.com</div>
    </div>
    <div class="back-band"></div>
  </section>
</body>
</html>
```